Plumbing company needs Business Card Design

Hi I need business card design based on logo which I uploaded. Its plumbing and heating company called Kranex Usługi Hydrauliczno-Gazowe. I want to see on my card motto of my company which is "...od wymiany uszczelki po wymiane łazienki.", my phone number, name, and website: 617248390, Marek Kowalczyk, info@kranex.org, www.kranex.org
I want to see logos of companys which I'm approved installer (Termolux) (La Valmont) (Corvo) (Pluma).
I want new creative look of business card. I like rounded corners.
Any questions please send message.
Thanks for intrest.
Business
Contact Information for Business Card
Marek Kowalczyk
617 248 390
info@kranex.org
www.kranex.org
...od wymiany uszczelki po wymiane łazienki.

```html
<!DOCTYPE html>
<html lang="pl">
<head>
<meta charset="utf-8">
<title>Kranex – wizytówka</title>
<link rel="stylesheet" href="https://fonts.googleapis.com/css2?family=Exo+2:wght@700;800&family=Open+Sans:wght@400;600&display=swap">
<style>
  :root {
    --navy: #1c3f8f;
    --navy-deep: #16347a;
    --red: #e0141e;
    --yellow: #f6e21a;
    --paper: #f6f6f4;
    --ink-grey: #4a4a4a;
    --stage: #e9e6df;
  }
  * { box-sizing: border-box; margin: 0; padding: 0; }
  html, body { width: 1200px; height: 840px; overflow: hidden; }
  body {
    background: var(--stage);
    display: flex;
    align-items: center;
    justify-content: center;
    gap: 60px;
    font-family: "Open Sans", Arial, sans-serif;
  }
  .card {
    width: 500px;
    height: 500px;
    border-radius: 34px;
    overflow: hidden;
    position: relative;
    box-shadow: 0 10px 30px rgba(0,0,0,.18);
  }

  /* Front */
  .card--front { background: var(--paper); }
  .brand { position: absolute; left: 36px; top: 40px; display: flex; align-items: center; gap: 18px; }
  .brand__mark { width: 112px; height: 84px; background: var(--yellow); border-radius: 14px; }
  .brand__name {
    font-family: "Exo 2", Arial, sans-serif; font-weight: 800;
    font-size: 56px; line-height: 1; color: var(--red);
  }
  .brand__tagline {
    font-family: "Exo 2", Arial, sans-serif; font-weight: 700;
    font-size: 19px; color: var(--navy); margin-top: 6px;
  }
  .person {
    position: absolute; left: 40px; top: 168px;
    font-family: "Exo 2", Arial, sans-serif; font-weight: 800;
    font-size: 27px; letter-spacing: 1.5px; color: var(--navy);
    text-transform: uppercase;
  }
  .contacts { position: absolute; left: 40px; top: 226px; list-style: none; }
  .contacts li {
    display: flex; align-items: center; gap: 14px;
    font-size: 20px; color: var(--ink-grey); height: 34px;
  }
  .icon { width: 24px; height: 24px; border-radius: 5px; background: var(--red); display: flex; align-items: center; justify-content: center; }
  .icon svg { width: 16px; height: 16px; fill: none; stroke: #fff; stroke-width: 2; }
  .front__band {
    position: absolute; left: 0; right: 0; bottom: 0; height: 150px;
    background: var(--navy);
    border-top: 6px solid var(--red);
  }
  .front__band::before {
    content: ""; position: absolute; left: 0; right: 0; top: 0; height: 6px; background: #fff;
  }
  .motto {
    position: absolute; left: 40px; right: 30px; top: 46px;
    color: #fff; font-size: 19px; line-height: 1.5;
  }

  /* Back */
  .card--back {
    background: var(--navy);
    display: flex; flex-direction: column; align-items: center; justify-content: center;
    text-align: center;
  }
  .back__mark { width: 170px; height: 130px; background: var(--yellow); border-radius: 22px; margin-bottom: 26px; }
  .back__name {
    font-family: "Exo 2", Arial, sans-serif; font-weight: 800;
    font-size: 76px; line-height: 1; color: var(--red);
  }
  .back__tagline {
    font-family: "Exo 2", Arial, sans-serif; font-weight: 700;
    font-size: 22px; color: #fff; margin-top: 8px;
  }
  .back__phone {
    display: flex; align-items: center; gap: 16px; margin-top: 34px;
    color: #fff; font-size: 38px; letter-spacing: 2px;
  }
  .back__phone .icon { width: 30px; height: 30px; }
  .back__phone .icon svg { width: 20px; height: 20px; }
</style>
</head>
<body>

  <section class="card card--front">
    <div class="brand">
      <span class="brand__mark"></span>
      <div>
        <div class="brand__name">Kranex</div>
        <div class="brand__tagline">Usługi Hydrauliczno-Gazowe</div>
      </div>
    </div>

    <h1 class="person">Marek Kowalczyk</h1>

    <ul class="contacts">
      <li><span class="icon"><svg viewBox="0 0 16 16"><path d="M4 2h2.5l1 3-1.5 1a7 7 0 0 0 3.5 3.5l1-1.5 3 1V12a2 2 0 0 1-2 2A10 10 0 0 1 2 4a2 2 0 0 1 2-2z"/></svg></span>617 248 390</li>
      <li><span class="icon"><svg viewBox="0 0 16 16"><rect x="2" y="4" width="12" height="9" rx="1"/><path d="M2 5l6 4 6-4"/></svg></span>info@kranex.org</li>
      <li><span class="icon"><svg viewBox="0 0 16 16"><circle cx="8" cy="8" r="6"/><path d="M2 8h12M8 2c-3 3-3 9 0 12M8 2c3 3 3 9 0 12"/></svg></span>www.kranex.org</li>
    </ul>

    <div class="front__band">
      <p class="motto">...od wymiany uszczelki po wymiane łazienki</p>
    </div>
  </section>

  <section class="card card--back">
    <span class="back__mark"></span>
    <div class="back__name">Kranex</div>
    <div class="back__tagline">Usługi Hydrauliczno-Gazowe</div>
    <div class="back__phone">
      <span class="icon"><svg viewBox="0 0 16 16"><path d="M4 2h2.5l1 3-1.5 1a7 7 0 0 0 3.5 3.5l1-1.5 3 1V12a2 2 0 0 1-2 2A10 10 0 0 1 2 4a2 2 0 0 1 2-2z"/></svg></span>
      617 248 390
    </div>
  </section>

</body>
</html>
```